Design a Sleek, Modern Insert Card for a Wellness-Inspired Clinical Kit

We are looking for a sleek, professional insert card design to include inside our KELVARO Trial Boost kits — curated wellness pouches that will be sent to clinical research coordinators, physicians, and nurses participating in our KELVARO clinical study.
This insert should visually reflect the MORANTH Biologics and KELVARO brands (logos attached) — clean, modern, and cohesive — and serve as a small note of appreciation for their work.
Insert Text (exact wording to include):
Everything inside was chosen to fuel your focus, KELVARO your energy, and support your work advancing disc restoration.
Design Requirements:
Size: Small insert card that fits neatly inside a zippered pouch (approx. 4” x 6” or similar).
Orientation: Landscape
Logos:
KELVARO logo
MORANTH Biologics logo
(Both should be tastefully included and balanced within the design.)
Color Palette:
Shades of blue (from the KELVARO logo)
Shades of green (from the MORANTH logo)
Design Style:
Modern, clean, and minimalistic
Professional and medical, but still visually engaging
Premium feel (this will be part of an elegant, high-end kit)
Typography:
Easy to read, sans-serif fonts (open to designer’s creative judgment)
Should align with a clinical or wellness aesthetic (not overly corporate or decorative)
Examples of brand aesthetics that inspire us: Quince packaging, Hush app, Brimwell Nutrients, or ZERKA hydration branding
Target Market(s)
Physicians & nurses
Industry/Entity Type
Medical
Look and feel

```html
<!DOCTYPE html>
<html lang="en">
<head>
<meta charset="utf-8">
<title>KELVARO Trial Boost Insert Card</title>
<link href="https://fonts.googleapis.com/css2?family=Lato:wght@400;700;900&display=swap" rel="stylesheet">
<style>
  :root {
    --sky-light: #d9ecf7;
    --sky-mid: #a9d4e8;
    --teal: #3f9ea6;
    --teal-deep: #2a8a93;
    --leaf: #6fa98c;
    --leaf-light: #cfe8c9;
    --marble: #f4f7fa;
    --marble-edge: #e6ecf1;
    --marble-shadow: #c9d2da;
    --ink: #111418;
    --brand-green: #6cb33f;
    --brand-navy: #1c2254;
  }
  * { margin: 0; padding: 0; box-sizing: border-box; }
  html, body { width: 1200px; height: 851px; overflow: hidden; }
  body { font-family: "Lato", sans-serif; background: var(--marble); }

  .insert-card {
    position: relative;
    width: 1200px;
    height: 851px;
    overflow: hidden;
  }

  .backdrop-photo {
    position: absolute;
    inset: 0 0 226px 0;
    background:
      radial-gradient(ellipse 260px 330px at 150px 390px, rgba(111,169,140,0.85), rgba(111,169,140,0) 70%),
      radial-gradient(ellipse 200px 260px at 1130px 120px, rgba(120,180,110,0.55), rgba(120,180,110,0) 70%),
      radial-gradient(ellipse 420px 300px at 1050px 480px, rgba(42,138,147,0.75), rgba(42,138,147,0) 75%),
      radial-gradient(ellipse 360px 220px at 180px 40px, rgba(240,248,252,0.9), rgba(240,248,252,0) 70%),
      linear-gradient(180deg, var(--sky-light) 0%, var(--sky-mid) 45%, var(--teal) 100%);
  }

  .marble-counter {
    position: absolute;
    left: 0; right: 0; bottom: 0;
    height: 226px;
    background: linear-gradient(180deg, #fbfdfe 0%, var(--marble) 60%, var(--marble-edge) 100%);
  }
  .marble-counter .front-edge {
    position: absolute;
    left: 0; right: 0; top: 145px; bottom: 0;
    background: linear-gradient(180deg, var(--marble-edge) 0%, #f2f5f8 40%, var(--marble-shadow) 100%);
  }

  .message {
    position: absolute;
    left: 352px;
    top: 254px;
    width: 770px;
    text-align: center;
    color: var(--ink);
    font-weight: 400;
    font-size: 43.5px;
    line-height: 57px;
    letter-spacing: -0.3px;
  }

  .brand-moranth {
    position: absolute;
    left: 192px;
    top: 656px;
    color: var(--brand-green);
    font-weight: 400;
    text-align: right;
  }
  .brand-moranth .name {
    display: block;
    font-size: 66px;
    line-height: 70px;
    letter-spacing: -1px;
  }
  .brand-moranth .division {
    display: block;
    font-size: 15px;
    line-height: 18px;
    letter-spacing: 0.5px;
  }

  .brand-kelvaro {
    position: absolute;
    left: 690px;
    top: 678px;
    color: var(--brand-navy);
    font-weight: 900;
  }
  .brand-kelvaro .lockup {
    display: flex;
    align-items: center;
    gap: 10px;
  }
  .brand-kelvaro .mark {
    width: 28px;
    height: 28px;
    background: var(--brand-navy);
  }
  .brand-kelvaro .name {
    font-size: 54px;
    line-height: 60px;
    letter-spacing: -0.5px;
  }
  .brand-kelvaro .trial-line {
    display: block;
    margin-left: 52px;
    font-size: 8.5px;
    font-weight: 700;
    line-height: 12px;
    color: var(--brand-navy);
  }
</style>
</head>
<body>
  <main class="insert-card">
    <div class="backdrop-photo" role="img" aria-label="Soft-focus photo of eucalyptus sprigs on the left against a blurred blue and teal garden background"></div>
    <div class="marble-counter" role="img" aria-label="White marble countertop">
      <div class="front-edge"></div>
    </div>

    <p class="message">Everything inside was chosen to fuel your focus, KELVARO your energy, and support your work advancing disc restoration.</p>

    <div class="brand-moranth">
      <span class="name">MORANTH</span>
      <span class="division">BIOLOGICS</span>
    </div>

    <div class="brand-kelvaro">
      <div class="lockup">
        <span class="mark"></span>
        <span class="name">KELVARO U.S.</span>
      </div>
      <span class="trial-line">NUVEL Disc NP Randomized, Sham-Controlled, Multi-Center, Double Blind Clinical Trial</span>
    </div>
  </main>
</body>
</html>
```